Web Design Project

We are re-starting this project.

This project is for a totally new look and design of a website for Wablor. www.wablor-demo.net.

Wablor is a naming protocol for physical locations and can be used for fixed and mobile people, places and things. Find your friends, or find a business. Because Wablor locations point to precise geo-physical (GPS) co-ordinates, navigation to a location becomes totally reliable.
Updates

Please see the modified brief for this project

Target Market(s)

Every person and every business can have multiple !Wabs (Wablor locations), so the website needs to be appealing and fun, but easy to use and functional

Industry/Entity Type

Business

Colors
34a6d7

Requirements
Must have
• Uniqueness!

```html
<!DOCTYPE html>
<html lang="en">
<head>
<meta charset="utf-8">
<title>Wablor — Find people, places and things</title>
<link href="https://fonts.googleapis.com/css2?family=Roboto+Condensed:wght@400;700&display=swap" rel="stylesheet">
<style>
  :root {
    --sky-light: #b9d3d8;
    --sky-mid: #6aa7c6;
    --sky-deep: #3f7fae;
    --charcoal: #2f2f30;
    --charcoal-dark: #1f1f20;
    --white: #ffffff;
    --accent-blue: #34a6d7;
    --accent-pink: #e8559c;
    --placeholder: #9a9a9a;
    --photo-neutral-a: #c9d6dc;
    --photo-neutral-b: #a9bcc6;
  }
  * { margin: 0; padding: 0; box-sizing: border-box; }
  html, body { width: 1200px; height: 1000px; overflow: hidden; }
  body {
    font-family: "Roboto Condensed", "Arial Narrow", sans-serif;
    color: var(--white);
    position: relative;
  }
  .backdrop {
    position: absolute; inset: 0;
    background:
      radial-gradient(ellipse at 30% 0%, rgba(220,230,226,0.85) 0%, rgba(220,230,226,0) 45%),
      linear-gradient(160deg, var(--sky-light) 0%, var(--sky-mid) 40%, var(--sky-deep) 80%, #5a86a8 100%);
  }
  .menu-corner { position: absolute; left: 0; top: 0; }
  .menu-label {
    position: absolute; left: 34px; top: 88px;
    font-size: 12px; font-weight: 700;
  }
  .menu-label::after {
    content: ""; position: absolute; left: 8px; top: 18px;
    border-left: 5px solid transparent; border-right: 5px solid transparent;
    border-top: 5px solid var(--accent-blue);
  }
  .account-links {
    position: absolute; right: 72px; top: 88px;
    font-size: 12px; font-weight: 700;
  }
  .account-links .divider { margin: 0 5px; }
  .photo { position: absolute; border-radius: 50%; }
  .photo-resort { left: 375px; top: 375px; width: 114px; height: 114px;
    background: radial-gradient(circle at 50% 40%, #7fa6bc, #2d4a5a 80%); }
  .photo-lounge { left: 363px; top: 510px; width: 128px; height: 128px;
    background: radial-gradient(circle at 40% 40%, #86a846, #3a3a22 80%); }
  .photo-beach { left: 737px; top: 378px; width: 159px; height: 159px;
    background: radial-gradient(circle at 50% 50%, var(--photo-neutral-a), var(--photo-neutral-b) 90%); }
  .finder { position: absolute; left: 427px; top: 327px; }
  .brand {
    position: absolute; left: 495px; top: 362px; width: 212px;
    font-size: 50px; font-weight: 700; line-height: 1;
    display: flex; align-items: center; justify-content: center; gap: 8px;
  }
  .brand .mark { width: 14px; height: 14px; border-radius: 50%; background: var(--white); }
  .finder-question {
    position: absolute; left: 427px; width: 346px; top: 467px;
    text-align: center; font-size: 17px; letter-spacing: -0.2px;
  }
  .finder-question strong { color: var(--accent-pink); }
  .finder-input {
    position: absolute; left: 512px; top: 503px; width: 177px; height: 29px;
    background: var(--white); color: var(--placeholder);
    font-size: 16px; text-align: center; line-height: 29px;
  }
  .finder-button {
    position: absolute; left: 558px; top: 552px; width: 84px; height: 31px;
    background: var(--accent-blue); color: var(--white);
    font-size: 15px; font-weight: 700; text-align: center; line-height: 31px;
  }
  .about-link {
    position: absolute; left: 707px; top: 583px;
    font-size: 14px; line-height: 18px;
  }
  .about-link strong { font-weight: 700; font-size: 14.5px; letter-spacing: 0.3px; }
  .about-link .tm { font-weight: 400; }
  .about-link .arrow {
    display: inline-block; margin-left: 4px;
    border-top: 4px solid transparent; border-bottom: 4px solid transparent;
    border-left: 6px solid var(--accent-pink);
  }
  .updates-link {
    position: absolute; left: 500px; width: 200px; top: 691px;
    text-align: center; font-size: 14px;
  }
  .updates-link::after {
    content: ""; position: absolute; left: 96px; top: 19px;
    border-left: 4px solid transparent; border-right: 4px solid transparent;
    border-top: 4px solid var(--accent-pink);
  }
  .footer { position: absolute; right: 110px; top: 913px; text-align: right; }
  .footer .powered { font-size: 11px; opacity: 0.9; letter-spacing: 0.3px; }
  .footer .powered strong { font-size: 13px; }
  .footer .rights { font-size: 11px; font-weight: 700; margin-top: 3px; }
</style>
</head>
<body>
  <div class="backdrop"></div>

  <svg class="menu-corner" width="122" height="220" viewBox="0 0 122 220" aria-hidden="true">
    <polygon points="0,0 24,0 118,96 2,214 0,214" fill="#5c5c5c"/>
    <polygon points="0,0 20,0 114,96 0,210" fill="var(--charcoal)"/>
  </svg>
  <div class="menu-label">MENU</div>

  <div class="account-links">SIGN UP<span class="divider">|</span>LOGIN</div>

  <div class="photo photo-resort" role="img" aria-label="Photo of a tropical resort pool with palm trees"></div>
  <div class="photo photo-lounge" role="img" aria-label="Photo of a green-lit lounge interior"></div>

  <svg class="finder" width="346" height="346" viewBox="0 0 346 346" aria-hidden="true">
    <defs>
      <linearGradient id="finderFill" x1="0" y1="0" x2="0" y2="1">
        <stop offset="0" stop-color="var(--charcoal)"/>
        <stop offset="1" stop-color="var(--charcoal-dark)"/>
      </linearGradient>
    </defs>
    <polygon points="173,0 346,173 173,346 0,173" fill="url(#finderFill)"/>
  </svg>

  <div class="photo photo-beach" role="img" aria-label="Photo of a sunny beach scene"></div>

  <div class="brand"><span class="mark"></span>Wablor</div>
  <div class="finder-question">WHO WOULD YOU LIKE TO <strong>FIND</strong>?</div>
  <div class="finder-input">FIND !Wab...</div>
  <div class="finder-button">LOOK UP</div>

  <div class="about-link">
    WHAT IS THIS<br>
    <strong>WABLOR</strong><span class="tm">™</span> <strong>SOCIAL POSITIONING</strong><br>
    PHENOMENON?<span class="arrow"></span>
  </div>

  <div class="updates-link">SEE <strong>UPDATES</strong></div>

  <div class="footer">
    <div class="powered">powered by <strong>Wablor API</strong></div>
    <div class="rights">ALL RIGHTS RESERVED</div>
  </div>
</body>
</html>
```